Create a Graphic About YOURSELF and PixelHarbor

PixelHarbor would like you (designers) to create an awesome graphic to promote YOURSELF and your profile on PixelHarbor!

Your graphic should communicate your name, your services and should mention PixelHarbor.

The design should be perfect for sharing on Chatterly. Here's an example of what we'd like http://blog.pixelharbor-example.ca/article/333/pixelharbor-launches-3000-hire-me-social-design-contest

Once you submitted your design, we'd love you to share the design ('advertisement') and promote yourself and PixelHarbor to your friends and potential customers. So make your submissions great and get your friends to vote for your design by 'Liking' it on Chatterly!

Prizes:
$1500 - "PixelHarbor Community" prize awarded to the designer with the most Chatterly 'Likes'
5 x $50 for the next 5 'most liked' designs on Chatterly

$1000 - "Hire Me" prize awarded to the designer who receives the most client invites
5 x $50 for the next 5 'most invited' designers

In summary, this is a great opportunity for you to increase your exposure to PixelHarbor customers and win cash prizes. Show off your design skills and get hired by PixelHarbor customers from around the world!

Target Market(s)

Fans, friends and customers of YOU

Industry/Entity Type

Cash

Requirements
Must have
• 1) Include your PixelHarbor user name on the graphic so customers can find you in the PixelHarbor Designer Directory
2) Include the tagline "Hire Me on PixelHarbor.com!" in your graphic design.
3) Share your design's URL on our Chatterly wall at http://chatterly-example.com/pixelharbor and get your friends to 'like' your design.
Nice to have
• 1) Include a tagline that expresses your design approach/philosophy
2) Artwork dimensions: 403 x 403 px
3) You can submit more than 1 design!
Should not have
• You must own the copyright of any images you use including stock imagery.

```html
<!DOCTYPE html>
<html lang="en">
<head>
<meta charset="utf-8">
<title>Cherished Mementos – Hire Me On PixelHarbor.com</title>
<link rel="stylesheet" href="https://fonts.googleapis.com/css2?family=Crimson+Pro:wght@400;600&display=swap">
<style>
  :root {
    --field-green: #3ad400;
    --frame-pale: #d6f79c;
    --bloom-red: #c0292c;
    --bloom-light: #4fd24a;
    --ink: #0b0b0b;
    --ink-wine: #3a0a10;
  }
  html, body {
    margin: 0;
    padding: 0;
    overflow: hidden;
  }
  .poster {
    position: relative;
    width: 1200px;
    height: 900px;
    overflow: hidden;
    background: var(--field-green);
    box-shadow: inset 0 0 40px 22px var(--frame-pale);
    font-family: "Crimson Pro", Georgia, serif;
    color: var(--ink);
  }
  .bloom {
    position: absolute;
    left: 0;
    top: 0;
  }
  .side-tagline {
    position: absolute;
    left: 0;
    top: 28px;
    width: 48px;
    height: 620px;
    margin: 0;
    writing-mode: vertical-rl;
    font-size: 44px;
    font-weight: 400;
    line-height: 48px;
    letter-spacing: 27px;
    white-space: nowrap;
  }
  .site-address {
    position: absolute;
    left: 22px;
    right: 60px;
    bottom: 4px;
    margin: 0;
    display: flex;
    justify-content: space-between;
    font-size: 50px;
    font-weight: 600;
    line-height: 1;
  }
  .brand-name {
    position: absolute;
    left: 0;
    width: 1200px;
    top: 245px;
    margin: 0;
    text-align: center;
    font-size: 104px;
    font-weight: 600;
    line-height: 1;
  }
  .byline {
    position: absolute;
    left: 430px;
    width: 300px;
    top: 462px;
    margin: 0;
    text-align: center;
    font-size: 21px;
    line-height: 25px;
  }
  .service {
    position: absolute;
    margin: 0;
    font-size: 25px;
    font-weight: 600;
    letter-spacing: 0.5px;
    color: var(--ink-wine);
    white-space: nowrap;
    transform: translate(-50%, -50%) rotate(var(--tilt));
  }
</style>
</head>
<body>
<main class="poster">
  <svg class="bloom" width="1200" height="900" viewBox="0 0 1200 900">
    <defs>
      <radialGradient id="bloomFill" cx="50%" cy="50%" r="50%">
        <stop offset="0" stop-color="var(--bloom-light)"/>
        <stop offset="0.22" stop-color="var(--bloom-light)"/>
        <stop offset="0.34" stop-color="var(--bloom-red)"/>
        <stop offset="0.86" stop-color="var(--bloom-red)"/>
        <stop offset="1" stop-color="var(--bloom-red)" stop-opacity="0"/>
      </radialGradient>
    </defs>
    <ellipse role="img" aria-label="Large red flower of pointed petals with pale green overlaps radiating from the centre" cx="612" cy="435" rx="575" ry="440" fill="url(#bloomFill)"/>
  </svg>

  <h2 class="side-tagline">Hire Me On</h2>

  <h1 class="brand-name">Cherished Mementos</h1>
  <p class="byline">by<br>Renata Vale</p>

  <p class="service" style="left:248px; top:565px; --tilt:-25deg;">Poster Designs</p>
  <p class="service" style="left:352px; top:652px; --tilt:-60deg;">Stationery Designs</p>
  <p class="service" style="left:480px; top:683px; --tilt:-80deg;">Business Card Designs</p>
  <p class="service" style="left:620px; top:672px; --tilt:65deg;">T-Shirt Designs</p>
  <p class="service" style="left:757px; top:700px; --tilt:75deg;">Logo Designs</p>
  <p class="service" style="left:875px; top:623px; --tilt:55deg;">and more…</p>

  <p class="site-address" aria-label="PixelHarbor.com">
    <span>P</span><span>i</span><span>x</span><span>e</span><span>l</span><span>H</span><span>a</span><span>r</span><span>b</span><span>o</span><span>r</span><span>.</span><span>c</span><span>o</span><span>m</span>
  </p>
</main>
</body>
</html>
```